Grain Clear Kitchen Web Design

We are looking for designs for a homepage for a gluten free, health food website.

We are looking for the site to be a shop, as well as a resource/information source for users. We will also look to incorporate recipes, blogs, forums and potentially some other useful information.

We want to ensure that the website is user-friendly, does not have a corporate feel, but is still classy.

We want to have high quality photographic images in the background, with text in the foreground - but these things will need to compliment each other well. e.g recipe of the week integrated onto the background photo and the 'shop' in the foreground.

We have seen a site that we quite like and although we like the design, we do not want to completely emulate this. However, it is a useful starting point for designers and perhaps some inspiration www.brightpantryhall.example

We already have a logo - see attached - which will need to be fully integrated into the design.

We do want a colourful design, but mainly in terms of the images rather than the graphics.
Updates

Please note:

We are pleased with the designs to date, for the most part. We would like you all to note, however, that we are much preferring the lighter designs - ones that make the sites feel brighter - rather than those which are darker in appearance.

We would also like to see less space allocated to the main image, within the context of the site as a whole.

Thanks.

We have eliminated those which we feel are not what we are looking for. We are still keen to see some more designs and are still looking for something unique. There are some good things in all of the designs that we have not eliminated, however we still feel there is room for more inspiration.

Thanks.

Target Market(s)

Our audience are body conscience people looking for health food products. They are also those who are potentially looking for a new lifestyle/life cha

Industry/Entity Type

Health

Requirements
Must have
• Our logo - attached, can provide variations in due course.

Navigational features as per mock up attached.

Social network integration.

NB: we only need one (home) page for this.

```html
<!DOCTYPE html>
<html lang="en">
<head>
<meta charset="utf-8">
<title>Grain Clear Kitchen</title>
<link rel="stylesheet" href="https://fonts.googleapis.com/css2?family=Arimo:wght@400;700&family=Lobster&family=Rubik+Dirt&display=swap">
<style>
  :root {
    --red: #c8101b;
    --red-dark: #8e0a10;
    --wood: #1d1b1a;
    --wood-light: #2a2725;
    --ink: #333333;
    --muted: #777777;
    --panel: #ffffff;
    --panel-grey: #eeeeee;
    --sky: #2ea6e8;
    --white: #ffffff;
    --tab: #2b2b2b;
  }
  * { margin: 0; padding: 0; box-sizing: border-box; }
  html, body { width: 1200px; height: 1063px; overflow: hidden; }
  body {
    position: relative;
    font-family: "Arimo", Arial, sans-serif;
    background: repeating-linear-gradient(90deg, var(--wood) 0 7px, var(--wood-light) 7px 9px, var(--wood) 9px 23px, #242120 23px 25px);
    color: var(--ink);
  }
  .abs { position: absolute; }

  /* hero */
  .hero-photo {
    left: 0; top: 0; width: 1200px; height: 463px;
    background:
      radial-gradient(ellipse 380px 170px at 680px 340px, #e0a349 0%, #c9852e 45%, rgba(120,90,40,0) 100%),
      radial-gradient(ellipse 500px 260px at 900px 160px, #5f7e6d 0%, rgba(60,80,60,0) 100%),
      linear-gradient(180deg, #4d5a3e 0%, #6b7a4e 40%, #3c4a2b 100%);
  }
  .top-nav { left: 768px; top: 16px; display: flex; gap: 14px; font-size: 11px; color: var(--white); line-height: 16px; white-space: nowrap; }
  .search {
    left: 915px; top: 12px; width: 179px; height: 23px; border-radius: 12px;
    background: var(--white); font-size: 11px; color: #666; padding: 4px 12px;
  }
  .search svg { position: absolute; right: 10px; top: 6px; }

  .side-nav {
    left: 106px; top: 103px; width: 196px; height: 360px; background: var(--red);
    box-shadow: 0 0 10px rgba(0,0,0,.5);
  }
  .brand {
    left: 0; top: 22px; width: 196px; text-align: center;
    font-weight: 700; font-size: 17px; color: var(--white); line-height: 20px;
  }
  .nav-list { list-style: none; position: absolute; left: 0; top: 104px; width: 196px; text-align: center; }
  .nav-list li {
    font-family: "Rubik Dirt", sans-serif; color: var(--white); font-size: 26px; line-height: 38px;
    text-shadow: 0 2px 2px rgba(0,0,0,.4);
  }
  .follow {
    left: 144px; top: 452px; width: 118px; height: 56px; border-radius: 0 0 59px 59px;
    background: var(--red); text-align: center; z-index: 2;
  }
  .follow p { font-family: "Lobster", sans-serif; color: var(--white); font-size: 14px; line-height: 16px; margin-top: 6px; }
  .follow .dots { display: flex; justify-content: center; gap: 5px; margin-top: 4px; }
  .follow .dots span { width: 13px; height: 13px; border-radius: 50%; background: var(--white); }

  .sub-nav {
    left: 302px; top: 274px; width: 152px; height: 134px; background: rgba(235,235,235,.93);
    list-style: none; padding: 8px 18px;
  }
  .sub-nav li { font-size: 12px; color: #444; line-height: 29px; border-bottom: 1px solid #d3d3d3; }
  .sub-nav li:last-child { border-bottom: 0; }

  .week-title {
    left: 497px; top: 160px; font-family: "Lobster", sans-serif; font-size: 56px; color: var(--white);
    text-shadow: 0 2px 6px rgba(0,0,0,.5); line-height: 64px; font-weight: 400;
  }
  .week-banner {
    left: 535px; top: 235px; width: 327px; height: 43px; background: var(--red);
    color: var(--white); font-size: 22px; line-height: 43px; text-align: center;
  }
  .shop-now {
    left: 588px; top: 278px; width: 218px; height: 34px; background: var(--tab);
    color: var(--white); font-weight: 700; font-size: 17px; text-align: center; line-height: 32px;
  }
  .slider-dots { left: 1045px; top: 434px; display: flex; gap: 5px; }
  .slider-dots span { width: 9px; height: 9px; border-radius: 50%; background: #cfcfcf; }
  .slider-dots span.on { background: #333; border: 2px solid #ddd; }

  /* content */
  .section-title {
    font-family: "Rubik Dirt", sans-serif; color: var(--white); font-size: 21px; letter-spacing: 1px; line-height: 24px; font-weight: 400;
  }
  .arrows { display: flex; gap: 4px; }
  .arrows span { width: 13px; height: 13px; border-radius: 50%; background: #555; }
  .arrows span.on { background: #bbb; }

  .featured-photo {
    left: 312px; top: 540px; width: 285px; height: 285px;
    background: radial-gradient(ellipse at 50% 45%, #c9a070 0%, #6f9a48 40%, #3f6b2a 75%, #e8ece6 100%);
  }
  .ribbon {
    height: 32px; background: var(--red); color: var(--white); font-size: 17px; line-height: 32px; padding-left: 20px;
    clip-path: polygon(0 0, 100% 0, 93% 50%, 100% 100%, 0 100%);
  }

  .blog-panel { left: 612px; top: 540px; width: 482px; height: 285px; background: var(--panel); }
  .blog-card { position: absolute; top: 10px; width: 219px; height: 265px; background: var(--panel-grey); }
  .blog-card .photo { width: 219px; height: 137px; }
  .blog-card h3 { font-weight: 400; color: var(--red); font-size: 14px; margin: 14px 11px 6px; }
  .blog-card p { font-size: 10.5px; color: #555; line-height: 14px; margin: 0 11px; }
  .blog-card .meta {
    position: absolute; left: 11px; right: 11px; bottom: 10px; font-size: 10px; color: var(--muted);
    display: flex; justify-content: space-between; align-items: center; white-space: nowrap;
  }
  .blog-card .meta b { font-weight: 400; color: #333; font-size: 11px; }

  .tweet-icon { left: 306px; top: 826px; width: 20px; height: 20px; border-radius: 50%; background: var(--sky); }
  .tweet-box { left: 312px; top: 840px; width: 285px; height: 110px; background: var(--sky); padding: 20px 14px; color: var(--white); }
  .tweet-box h4 { font-weight: 400; font-size: 13px; margin-bottom: 6px; }
  .tweet-box p { font-size: 11px; line-height: 15px; opacity: .85; }

  .forum { left: 612px; top: 840px; width: 482px; height: 110px; background: var(--panel); }
  .forum-head {
    height: 27px; background: var(--red); color: var(--white); display: flex; align-items: center; font-size: 13px;
  }
  .forum-head .f-title { width: 314px; padding-left: 16px; }
  .forum-head .f-replies { width: 60px; text-align: center; font-size: 11px; }
  .forum-head .f-last { flex: 1; text-align: center; font-size: 11px; }
  .forum-row { display: flex; height: 83px; }
  .forum-row .f-title { width: 314px; padding: 8px 16px; border-right: 1px solid #e2e2e2; }
  .forum-row h4 { color: var(--red); font-weight: 400; font-size: 14px; margin-bottom: 3px; }
  .forum-row p { font-size: 10.5px; color: #555; line-height: 14px; }
  .forum-row .f-replies { width: 60px; border-right: 1px solid #e2e2e2; text-align: center; font-size: 11px; padding-top: 26px; }
  .forum-row .f-last { flex: 1; text-align: center; font-size: 10.5px; padding-top: 26px; white-space: nowrap; }

  .footer-line { left: 0; top: 1000px; width: 1200px; height: 1px; background: #333; }
  .footer-nav { left: 106px; top: 1023px; display: flex; gap: 20px; font-size: 11.5px; color: #ddd; }
</style>
</head>
<body>
  <header>
    <div class="abs hero-photo" role="img" aria-label="Close-up photo of a golden baked chipotle burger with melted cheese on a green plate, fork to the side"></div>
    <nav class="abs top-nav"><span>Home</span><span>Log in</span><span>Contact Us</span></nav>
    <div class="abs search">Search
      <svg width="10" height="10" viewBox="0 0 10 10"><circle cx="4" cy="4" r="3" fill="none" stroke="#aaa" stroke-width="1.4"/><line x1="6.3" y1="6.3" x2="9.3" y2="9.3" stroke="#aaa" stroke-width="1.4"/></svg>
    </div>

    <nav class="abs side-nav">
      <div class="abs brand">Grain Clear<br>Kitchen</div>
      <ul class="nav-list">
        <li>Shop</li><li>Our Story</li><li>Blog</li><li>Hints &amp; Tips</li><li>Recipes</li><li>Forums</li>
      </ul>
    </nav>
    <div class="abs follow">
      <p>Follow us on</p>
      <div class="dots"><span></span><span></span><span></span><span></span></div>
    </div>
    <ul class="abs sub-nav">
      <li>Kids Pizza</li><li>Gluten Free sCones</li><li>Organic Food</li><li>Summer Foods</li>
    </ul>

    <h1 class="abs week-title">Recipe Of The Week</h1>
    <div class="abs week-banner">Chipotle Burger - $1.99 a pint</div>
    <div class="abs shop-now">Shop Now
      <svg width="14" height="14" viewBox="0 0 14 14" style="vertical-align:-2px"><circle cx="7" cy="7" r="7" fill="#fff"/><path d="M5.5 4 L9 7 L5.5 10" fill="none" stroke="#2b2b2b" stroke-width="2"/></svg>
    </div>
    <div class="abs slider-dots"><span></span><span class="on"></span><span></span></div>
  </header>

  <main>
    <h2 class="abs section-title" style="left:312px;top:510px">Featured Recipe</h2>
    <div class="abs arrows" style="left:568px;top:515px"><span></span><span class="on"></span></div>
    <div class="abs featured-photo" role="img" aria-label="Photo of gluten free lettuce wraps filled with grains, tomato and greens"></div>
    <div class="abs ribbon" style="left:305px;top:742px;width:141px">Wrapped</div>
    <div class="abs ribbon" style="left:305px;top:782px;width:141px">Traditionally</div>

    <h2 class="abs section-title" style="left:612px;top:510px">Blogs</h2>
    <div class="abs arrows" style="left:1064px;top:515px"><span></span><span class="on"></span></div>
    <section class="abs blog-panel">
      <article class="blog-card" style="left:12px">
        <div class="photo" role="img" aria-label="Photo of fresh strawberries and blueberries" style="background:radial-gradient(circle at 40% 55%, #e02a2a 0%, #b3131b 45%, #3a2a50 100%)"></div>
        <h3>Blueberries on Sale Today Only</h3>
        <p>Lorem Ipsum is simply dummy text of the printing and typesetting industry. Lorem Ipsum has been the industry's standard dummy text ever since...</p>
        <div class="meta"><span>&#9635; MAY, 31, 2013</span><b>by Mara Ellison</b></div>
      </article>
      <article class="blog-card" style="left:252px">
        <div class="photo" role="img" aria-label="Photo of a pita stuffed with grated carrot and fresh vegetables" style="background:radial-gradient(circle at 45% 55%, #e6823a 0%, #d9a46a 45%, #c9b59a 100%)"></div>
        <h3>Get Your Morning Veggies</h3>
        <p>Lorem Ipsum is simply dummy text of the printing and typesetting industry. Lorem Ipsum has been the industry's standard dummy text ever since...</p>
        <div class="meta"><span>&#9635; MAY, 31, 2013</span><b>by Theo Lindqvist</b></div>
      </article>
    </section>

    <div class="abs tweet-icon"></div>
    <section class="abs tweet-box">
      <h4>Grain Clear Kitchen @grainclearkitchen</h4>
      <p>How wonderful, a gluten free travel agency. They pre-arrange gluten free travel arrangements... http://www.clearroutetravel.example</p>
    </section>

    <section class="abs forum">
      <div class="forum-head"><span class="f-title">Healthy Eating Forums</span><span class="f-replies">Replies</span><span class="f-last">Last Post</span></div>
      <div class="forum-row">
        <div class="f-title">
          <h4>Introductions &amp; Personal Stories</h4>
          <p>Healthy Eating Support Group members are welcome to introduce themselves. Tell your story, share experiences, success stories and failures.</p>
        </div>
        <div class="f-replies">12</div>
        <div class="f-last">03/15/2013 03:46 PM</div>
      </div>
    </section>
  </main>

  <footer>
    <div class="abs footer-line"></div>
    <nav class="abs footer-nav"><span>Contact</span><span>Site Map</span><span>FAQ's</span><span>Privacy Policy</span></nav>
  </footer>
</body>
</html>
```